STATIONERY and Brand ID for Tralven

We need a family of identical Brand guide
Call Card
Envelope
Letterhead
Poster
Brochure

It needs to have an international Fee/

The ARCHITECTURE/STRUCTURE must show the highest level of creativity

1. Call card could be two sided
2. cal card can have a a flap
3. Call card can have a curved edge

Target Market(s)

Business and bank clients

Industry/Entity Type

Bank

Requirements
Must have
• the logo atatched
• the colour scheme must be used
• There must be a common look and feel and they must have the same DNA

```html
<!DOCTYPE html>
<html lang="en">
<head>
<meta charset="utf-8">
<title>Tralven Stationery</title>
<link rel="stylesheet" href="https://fonts.googleapis.com/css2?family=Roboto:wght@400;500;700&display=swap">
<style>
:root{
  --navy:#0d2d6b;
  --green:#0a9a35;
  --lime:#7dc416;
  --stage:#5d6b7b;
  --paper:#ffffff;
  --ink:#333b45;
  --muted:#7a828c;
}
*{box-sizing:border-box;margin:0;padding:0}
html,body{width:1200px;height:881px;overflow:hidden;background:var(--paper);font-family:"Roboto",Arial,sans-serif;color:var(--ink)}
.canvas{position:relative;width:1200px;height:881px}
.stage{position:absolute;left:0;top:0;width:854px;height:881px;background:var(--stage)}
.row{position:absolute;left:0;width:854px;height:290px}
.row-green{top:0;--accent:var(--green)}
.row-navy{top:293px;--accent:var(--navy)}
.row-lime{top:586px;--accent:var(--lime)}

.wordmark{font-weight:700;color:var(--navy);letter-spacing:-.5px;white-space:nowrap;display:inline-flex;align-items:center;gap:.18em;line-height:1}
.wordmark::before{content:"";width:.55em;height:.55em;border-radius:50%;background:var(--green);flex:none}
.wordmark.on-color{color:#fff}
.wordmark.on-color::before{background:#fff}

/* letterhead */
.letterhead{position:absolute;left:13px;top:18px;width:186px;height:264px;background:var(--paper);font-size:3.4px;line-height:1.35;color:var(--muted)}
.letterhead .sender{position:absolute;left:9px;top:7px;color:var(--ink)}
.letterhead .wordmark{position:absolute;right:10px;top:12px;font-size:14px}
.letterhead .body{position:absolute;left:9px;top:68px;width:166px}
.letterhead .body p{margin-bottom:4px}
.letterhead .sign{margin-top:10px;font-size:4px;color:var(--ink)}
.band{position:absolute;left:0;bottom:0;width:100%;height:4px;display:flex}
.band i{display:block;height:100%}
.band .b1{width:60%;background:var(--navy)}
.band .b2{flex:1;background:var(--accent)}

/* folder */
.folder{position:absolute;left:210px;top:18px;width:187px;height:264px;background:var(--accent)}
.folder .wordmark{position:absolute;left:24px;top:120px;font-size:28px}
.folder .contact{position:absolute;left:134px;top:232px;font-size:3.2px;line-height:1.4;color:#fff}

/* envelopes */
.env-back{position:absolute;left:406px;top:25px;width:273px;height:117px;background:var(--paper)}
.env-back .wordmark{position:absolute;left:12px;top:17px;font-size:16px}
.env-back .contact{position:absolute;left:12px;top:88px;font-size:3.2px;line-height:1.4;color:var(--ink)}
.env-front{position:absolute;left:408px;top:157px;width:276px;height:120px;background:var(--paper)}
.env-front .flap{position:absolute;left:0;top:0;width:100%;height:42px;background:var(--accent);border-radius:0 0 22px 22px}
.env-front .wordmark{position:absolute;left:96px;top:14px;font-size:15px}

/* cards */
.card{position:absolute;left:706px;width:140px;height:78px;overflow:hidden}
.card-front{top:60px;background:var(--paper);border-radius:0 8px 0 0}
.card-front .wordmark{position:absolute;left:28px;top:12px;font-size:15px}
.card-front .lower{position:absolute;left:0;bottom:0;width:100%;height:37px;background:var(--accent);color:#fff}
.card-front .who{position:absolute;left:23px;top:15px;font-size:4.6px;font-weight:700;line-height:1.2}
.card-front .who small{display:block;font-size:2.6px;font-weight:400}
.card-front .info{position:absolute;left:72px;top:6px;font-size:2.8px;line-height:1.35}
.card-back{top:157px;background:var(--accent);border-radius:0 0 8px 0;display:flex;align-items:center;justify-content:center;color:#fff;font-size:14px;font-weight:500;letter-spacing:.3px}
.row-navy .card{left:698px}

/* signatures */
.sig{position:absolute;color:var(--ink);font-size:6.2px;line-height:1.45}
.sig .name{font-size:10px;font-weight:700;color:var(--navy);line-height:1.1}
.sig .title{font-size:4.8px;margin-bottom:2px}
.sig .rule{position:absolute;width:1px;background:#9aa3ad}
.sig .line{display:flex;align-items:center;gap:4px;white-space:nowrap}
.sig svg.ico{width:7px;height:7px;flex:none;fill:var(--navy)}
.sig .abs{position:absolute}
</style>
</head>
<body>
<svg width="0" height="0" style="position:absolute" aria-hidden="true">
  <symbol id="i-phone" viewBox="0 0 10 10"><path d="M2 1l2 2-1 1.3c.6 1.3 1.4 2.1 2.7 2.7L7 6l2 2-1.4 1.4C4.5 9.2.8 5.5.6 2.4z"/></symbol>
  <symbol id="i-fax" viewBox="0 0 10 10"><rect x="2.5" y="0.5" width="5" height="3"/><rect x="0.5" y="4" width="9" height="4" rx="1"/><rect x="2.5" y="7" width="5" height="2.5"/></symbol>
  <symbol id="i-mail" viewBox="0 0 10 10"><path d="M.5 2h9v6h-9z M.8 2.3L5 5.5l4.2-3.2" stroke="#fff" stroke-width=".6"/></symbol>
  <symbol id="i-web" viewBox="0 0 10 10"><circle cx="5" cy="5" r="4.5"/><path d="M.5 5h9M5 .5c-2 2.5-2 6.5 0 9M5 .5c2 2.5 2 6.5 0 9" stroke="#fff" stroke-width=".6" fill="none"/></symbol>
</svg>

<div class="canvas">
  <div class="stage">

    <section class="row row-green">
      <article class="letterhead">
        <div class="sender">18 Canal Row<br>Marlow, CA 92041<br>858 240 1177<br>post@samplemail.com<br>www.sample-site.com</div>
        <span class="wordmark">Tralven</span>
        <div class="body">
          <p>Your Ref: SP KMC</p>
          <p>1 Dec 2014</p>
          <p>Mr Name of client<br>Designation<br>XYZ company ltd<br>Level 10<br>Address<br>MELBOURNE VIC 3000</p>
          <p>Thank you for the chance to present our proposal for the scope and nature of support we can offer your company in the coming year across all our business services.</p>
          <p>We value this partnership and look forward to working closely with your team.</p>
          <p>Our commitment is to deliver dependable banking solutions that help your organisation grow with confidence every day.</p>
          <div class="sign">A. Morel</div>
        </div>
        <div class="band"><i class="b1"></i><i class="b2"></i></div>
      </article>
      <article class="folder">
        <span class="wordmark on-color">Tralven</span>
        <div class="contact">18 Canal Row<br>Marlow, CA 92041<br>858 240 1177<br>post@samplemail.com<br>www.sample-site.com</div>
      </article>
      <article class="env-back">
        <span class="wordmark">Tralven</span>
        <div class="contact">18 Canal Row<br>Marlow, CA 92041<br>858 240 1177<br>post@samplemail.com<br>www.sample-site.com</div>
      </article>
      <article class="env-front"><div class="flap"><span class="wordmark on-color">Tralven</span></div></article>
      <article class="card card-front">
        <span class="wordmark">Tralven</span>
        <div class="lower">
          <div class="who">Mara Keane<small>General Manager - Saint Lucia</small></div>
          <div class="info"># 4 Harbour Lane, P O Box 2409<br>Castries, Saint Lucia<br>+17582013400<br>+17582013455<br>marakeane@tralven.bank<br>www.tralven.bank</div>
        </div>
      </article>
      <article class="card card-back">TRALVEN.bank</article>
    </section>

    <section class="row row-navy">
      <article class="letterhead">
        <div class="sender">18 Canal Row<br>Marlow, CA 92041<br>858 240 1177<br>post@samplemail.com<br>www.sample-site.com</div>
        <span class="wordmark">Tralven</span>
        <div class="body">
          <p>Your Ref: SP KMC</p>
          <p>1 Dec 2014</p>
          <p>Mr Name of client<br>Designation<br>XYZ company ltd<br>Level 10<br>Address<br>MELBOURNE VIC 3000</p>
          <p>Thank you for the chance to present our proposal for the scope and nature of support we can offer your company in the coming year across all our business services.</p>
          <p>We value this partnership and look forward to working closely with your team.</p>
          <p>Our commitment is to deliver dependable banking solutions that help your organisation grow with confidence every day.</p>
          <div class="sign">A. Morel</div>
        </div>
        <div class="band"><i class="b1"></i><i class="b2" style="background:var(--lime)"></i></div>
      </article>
      <article class="folder">
        <span class="wordmark on-color">Tralven</span>
        <div class="contact">18 Canal Row<br>Marlow, CA 92041<br>858 240 1177<br>post@samplemail.com<br>www.sample-site.com</div>
      </article>
      <article class="env-back">
        <span class="wordmark">Tralven</span>
        <div class="contact">18 Canal Row<br>Marlow, CA 92041<br>858 240 1177<br>post@samplemail.com<br>www.sample-site.com</div>
      </article>
      <article class="env-front"><div class="flap"><span class="wordmark on-color">Tralven</span></div></article>
      <article class="card card-front">
        <span class="wordmark">Tralven</span>
        <div class="lower">
          <div class="who">Mara Keane<small>General Manager - Saint Lucia</small></div>
          <div class="info"># 4 Harbour Lane, P O Box 2409<br>Castries, Saint Lucia<br>+17582013400<br>+17582013455<br>marakeane@tralven.bank<br>www.tralven.bank</div>
        </div>
      </article>
      <article class="card card-back">TRALVEN.bank</article>
    </section>

    <section class="row row-lime">
      <article class="letterhead">
        <div class="sender">18 Canal Row<br>Marlow, CA 92041<br>858 240 1177<br>post@samplemail.com<br>www.sample-site.com</div>
        <span class="wordmark">Tralven</span>
        <div class="body">
          <p>Your Ref: SP KMC</p>
          <p>1 Dec 2014</p>
          <p>Mr Name of client<br>Designation<br>XYZ company ltd<br>Level 10<br>Address<br>MELBOURNE VIC 3000</p>
          <p>Thank you for the chance to present our proposal for the scope and nature of support we can offer your company in the coming year across all our business services.</p>
          <p>We value this partnership and look forward to working closely with your team.</p>
          <p>Our commitment is to deliver dependable banking solutions that help your organisation grow with confidence every day.</p>
          <div class="sign">A. Morel</div>
        </div>
        <div class="band"><i class="b1"></i><i class="b2"></i></div>
      </article>
      <article class="folder">
        <span class="wordmark on-color">Tralven</span>
        <div class="contact">18 Canal Row<br>Marlow, CA 92041<br>858 240 1177<br>post@samplemail.com<br>www.sample-site.com</div>
      </article>
      <article class="env-back">
        <span class="wordmark">Tralven</span>
        <div class="contact">18 Canal Row<br>Marlow, CA 92041<br>858 240 1177<br>post@samplemail.com<br>www.sample-site.com</div>
      </article>
      <article class="env-front"><div class="flap"><span class="wordmark on-color">Tralven</span></div></article>
      <article class="card card-front">
        <span class="wordmark">Tralven</span>
        <div class="lower">
          <div class="who">Mara Keane<small>General Manager - Saint Lucia</small></div>
          <div class="info"># 4 Harbour Lane, P O Box 2409<br>Castries, Saint Lucia<br>+17582013400<br>+17582013455<br>marakeane@tralven.bank<br>www.tralven.bank</div>
        </div>
      </article>
      <article class="card card-back">TRALVEN.bank</article>
    </section>
  </div>

  <!-- email signatures -->
  <div class="sig" style="left:897px;top:50px;width:290px;height:96px">
    <span class="wordmark abs" style="left:0;top:0;font-size:34px">Tralven</span>
    <div class="abs" style="left:0;top:58px"><div class="name">Mara Keane</div><div class="title">General Manager - Saint Lucia</div></div>
    <i class="rule" style="left:70px;top:40px;height:52px"></i>
    <div class="abs" style="left:88px;top:40px">
      <div># 4 Harbour Lane, P O Box 2409<br>Castries, Saint Lucia</div>
      <div class="line"><svg class="ico"><use href="#i-phone"/></svg>+17582013400</div>
      <div class="line"><svg class="ico"><use href="#i-fax"/></svg>+17582013455</div>
      <div class="line"><svg class="ico"><use href="#i-mail"/></svg>marakeane@tralven.bank</div>
      <div class="line"><svg class="ico"><use href="#i-web"/></svg>www.tralven.bank</div>
    </div>
  </div>

  <div class="sig" style="left:902px;top:190px;width:290px;height:80px">
    <div class="name">Mara Keane</div><div class="title">General Manager - Saint Lucia</div>
    <span class="wordmark abs" style="left:0;top:32px;font-size:32px">Tralven</span>
    <i class="rule" style="left:176px;top:24px;height:52px"></i>
    <div class="abs" style="left:180px;top:22px">
      <div># 4 Harbour Lane, P O Box 2409<br>Castries, Saint Lucia</div>
      <div class="line"><svg class="ico"><use href="#i-phone"/></svg>+17582013400</div>
      <div class="line"><svg class="ico"><use href="#i-fax"/></svg>+17582013455</div>
      <div class="line"><svg class="ico"><use href="#i-mail"/></svg>marakeane@tralven.bank</div>
      <div class="line"><svg class="ico"><use href="#i-web"/></svg>www.tralven.bank</div>
    </div>
  </div>

  <div class="sig" style="left:910px;top:298px;width:280px;height:100px">
    <div class="name">Mara Keane</div><div class="title">General Manager - Saint Lucia</div>
    <div class="abs" style="left:0;top:28px"># 4 Harbour Lane, P O Box 2409<br>Castries, Saint Lucia</div>
    <i class="rule" style="left:105px;top:0;height:48px"></i>
    <div class="abs" style="left:114px;top:0">
      <div class="line"><svg class="ico"><use href="#i-phone"/></svg>+17582013400</div>
      <div class="line"><svg class="ico"><use href="#i-fax"/></svg>+17582013455</div>
      <div class="line"><svg class="ico"><use href="#i-mail"/></svg>marakeane@tralven.bank</div>
      <div class="line"><svg class="ico"><use href="#i-web"/></svg>www.tralven.bank</div>
    </div>
    <span class="wordmark abs" style="left:0;top:57px;font-size:33px">Tralven</span>
  </div>

  <div class="sig" style="left:910px;top:444px;width:280px;height:104px">
    <div class="name" style="font-size:12px">Mara Keane</div><div class="title">General Manager - Saint Lucia</div>
    <div class="abs" style="left:0;top:31px"># 4 Harbour Lane, P O Box 2409, Castries, Saint Lucia</div>
    <div class="abs" style="left:0;top:44px">
      <div class="line"><svg class="ico"><use href="#i-phone"/></svg>+17582013400</div>
      <div class="line"><svg class="ico"><use href="#i-fax"/></svg>+17582013455</div>
    </div>
    <i class="rule" style="left:78px;top:44px;height:26px"></i>
    <div class="abs" style="left:88px;top:44px">
      <div class="line"><svg class="ico"><use href="#i-mail"/></svg>marakeane@tralven.bank</div>
      <div class="line"><svg class="ico"><use href="#i-web"/></svg>www.tralven.bank</div>
    </div>
    <span class="wordmark abs" style="left:0;top:78px;font-size:22px">Tralven</span>
  </div>

  <div class="sig" style="left:910px;top:590px;width:280px;height:100px">
    <div class="name">Mara Keane</div><div class="title">General Manager - Saint Lucia</div>
    <span class="wordmark abs" style="left:0;top:28px;font-size:22px">Tralven</span>
    <div class="abs" style="left:0;top:58px"># 4 Harbour Lane, P O Box 2409, Castries, Saint Lucia</div>
    <div class="abs" style="left:0;top:70px">
      <div class="line"><svg class="ico"><use href="#i-phone"/></svg>+17582013400</div>
      <div class="line"><svg class="ico"><use href="#i-fax"/></svg>+17582013455</div>
    </div>
    <div class="abs" style="left:88px;top:70px">
      <div class="line"><svg class="ico"><use href="#i-mail"/></svg>marakeane@tralven.bank</div>
      <div class="line"><svg class="ico"><use href="#i-web"/></svg>www.tralven.bank</div>
    </div>
  </div>

  <div class="sig" style="left:910px;top:726px;width:280px;height:110px">
    <div class="name" style="font-size:12px">Mara Keane</div><div class="title">General Manager - Saint Lucia</div>
    <div class="abs" style="left:0;top:32px">
      <div class="line"><svg class="ico"><use href="#i-phone"/></svg>+17582013400</div>
      <div class="line"><svg class="ico"><use href="#i-fax"/></svg>+17582013455</div>
    </div>
    <i class="rule" style="left:78px;top:32px;height:26px"></i>
    <div class="abs" style="left:88px;top:32px">
      <div class="line"><svg class="ico"><use href="#i-mail"/></svg>marakeane@tralven.bank</div>
      <div class="line"><svg class="ico"><use href="#i-web"/></svg>www.tralven.bank</div>
    </div>
    <div class="abs" style="left:0;top:63px"># 4 Harbour Lane, P O Box 2409, Castries, Saint Lucia</div>
    <span class="wordmark abs" style="left:0;top:82px;font-size:22px">Tralven</span>
  </div>
</div>
</body>
</html>
```